Letterhead to Prospective Clients

Create a letterhead (word & canva) that I will use to send letters to prospective clients and also include the Coralwood Estate Partners Logo, My Contact Details and Interchangeable "Suburb". Use the same font and colour pallete

Maris Dulworth | "Suburb" Specialist - Redlands & Surrounds
Mobile: 0417 862 095
Email: MD@CoralwoodEstatePartners.com.au

```html
<!DOCTYPE html>
<html lang="en">
<head>
<meta charset="utf-8">
<title>Coralwood Estate Partners Letterhead</title>
<link rel="stylesheet" href="https://fonts.googleapis.com/css2?family=Open+Sans:wght@400;600&family=Outfit:wght@500&display=swap">
<style>
  :root {
    --navy: #0f1a3c;
    --tan: #d9a87c;
    --ink: #6b6b6b;
    --rule: #cfd2d6;
    --paper: #ffffff;
  }
  * { margin: 0; padding: 0; box-sizing: border-box; }
  html, body { width: 922px; height: 1200px; overflow: hidden; background: var(--paper); }
  .letterhead {
    position: relative;
    width: 922px;
    height: 1200px;
    background: var(--paper);
    font-family: "Open Sans", Arial, sans-serif;
    color: var(--ink);
  }
  .brand-name {
    position: absolute;
    left: 78px;
    top: 82px;
    font-size: 27px;
    font-weight: 400;
    letter-spacing: 0.06em;
    color: var(--navy);
  }
  .header-rule {
    position: absolute;
    left: 65px;
    top: 189px;
    width: 788px;
    height: 1px;
    background: var(--rule);
  }
  .sender {
    position: absolute;
    left: 65px;
    top: 210px;
  }
  .sender-name {
    font-size: 25px;
    font-weight: 600;
    color: var(--navy);
    line-height: 30px;
  }
  .sender-role {
    font-size: 13.5px;
    margin-top: 2px;
    line-height: 20px;
  }
  .sender-contact {
    list-style: none;
    margin-top: 6px;
    font-size: 16px;
    line-height: 27px;
  }
  .sender-contact .label {
    color: var(--tan);
    font-weight: 600;
    display: inline-block;
    width: 34px;
  }
  .letter-date {
    position: absolute;
    right: 83px;
    top: 432px;
    font-size: 17px;
  }
  .letter-body {
    position: absolute;
    left: 65px;
    top: 472px;
    width: 775px;
    font-size: 14.6px;
    line-height: 22.3px;
    text-align: justify;
  }
  .letter-body p + p { margin-top: 22px; }
  .signature-mark {
    position: absolute;
    left: 660px;
    top: 868px;
    width: 140px;
    height: 78px;
    background: linear-gradient(90deg, #f1f1f1, #e4e4e4);
  }
  .signatory {
    position: absolute;
    right: 100px;
    top: 958px;
    font-family: "Outfit", Arial, sans-serif;
    font-weight: 500;
    font-size: 22px;
    color: #2a2a2a;
  }
  .footer-contact {
    position: absolute;
    left: 65px;
    top: 1092px;
    list-style: none;
    font-size: 13px;
  }
  .footer-contact li {
    display: flex;
    align-items: center;
    gap: 6px;
    height: 26px;
  }
  .footer-contact svg { width: 16px; height: 16px; }
  .footer-bands {
    position: absolute;
    left: 0;
    bottom: 0;
    width: 922px;
    height: 38px;
  }
</style>
</head>
<body>
<div class="letterhead">
  <div class="brand-name">Coralwood Estate Partners</div>
  <div class="header-rule"></div>

  <section class="sender">
    <h1 class="sender-name">Maris Dulworth</h1>
    <p class="sender-role">"Suburb" Specialist - Redlands &amp; Surrounds</p>
    <ul class="sender-contact">
      <li><span class="label">P :</span>0417 862 095</li>
      <li><span class="label">M :</span>MD@CoralwoodEstatePartners.com.au</li>
    </ul>
  </section>

  <p class="letter-date">12 December, 2025</p>

  <main class="letter-body">
    <p>Lorem ipsum dolor sit amet, consectetuer adipiscing elit, sed diam nonummy nibh euismod tincidunt ut laoreet dolore magna aliquam erat volutpat. Ut wisi enim ad minim veniam, quis nostrud exerci tation ullamcorper suscipit lobortis nisl ut aliquip ex ea commodo consequat. Duis autem vel eum iriure dolor in hendrerit in vulputate velit esse molestie consequat, vel illum dolore eu feugiat nulla facilisis at vero eros et accumsan et iusto odio dignissim qui blandit praesent luptatum zzril delenit augue duis dolore te feugait nulla facilisi.</p>
    <p>Lorem ipsum dolor sit amet, cons ectetuer adipiscing elit, sed diam nonummy nibh euismod tincidunt ut laoreet dolore magna aliquam erat volutpat. Ut wisi enim ad minim veniam, quis nostrud exerci tation ullamcorper suscipit lobortis nisl ut aliquip ex ea commodo consequat.</p>
    <p>Lorem ipsum dolor sit amet, consectetuer adipiscing elit, sed diam nonummy nibh euismod tincidunt ut laoreet dolore magna aliquam eratveniam, quis nostrud exerci tation ullamcorper suscipit lobortis nisl ut aliquip ex ea commodo consequat. Lorem ipsum dolor sit zamet, consectetuer adipiscing elit, sed diam nonummy nibh euismod tincidunt.</p>
  </main>

  <div class="signature-mark" role="img" aria-label="Handwritten signature of Maris Dulworth"></div>
  <p class="signatory">Mr. Maris Dulworth</p>

  <ul class="footer-contact">
    <li>
      <svg viewBox="0 0 16 16" aria-hidden="true"><rect width="16" height="16" rx="3" fill="var(--tan)"/><path d="M5 3.5c.6 0 1.6 2 1.6 2.4 0 .5-.9.8-.8 1.3.3 1 1.3 2 2.1 2.3.5.1.8-.8 1.3-.8.5 0 2.4 1 2.4 1.6 0 .8-1 1.7-1.9 1.7C6.8 12 4 9.3 3.8 6.2 3.7 4.6 4.4 3.5 5 3.5z" fill="#fff"/></svg>
      0417 862 095
    </li>
    <li>
      <svg viewBox="0 0 16 16" aria-hidden="true"><rect width="16" height="16" rx="3" fill="var(--tan)"/><rect x="3" y="4.5" width="10" height="7" fill="none" stroke="#fff" stroke-width="1"/><path d="M3 4.5l5 4 5-4M3 11.5l3.6-3.3M13 11.5l-3.6-3.3" fill="none" stroke="#fff" stroke-width="1"/></svg>
      MD@CoralwoodEstatePartners.com.au
    </li>
  </ul>

  <svg class="footer-bands" viewBox="0 0 922 38" aria-hidden="true">
    <polygon points="0,17 762,17 753,27 0,27" fill="var(--tan)"/>
    <polygon points="782,0 922,0 922,38 0,38 0,32 754,32" fill="var(--navy)"/>
  </svg>
</div>
</body>
</html>
```